Investment Business - Biz Card Design

Using the attached logo files, please create a superior business card design for Brantwell Holdings.

The "back" of the card should feature the logo (either in colour, or white/black over a feature colour)

The "front" of the card should feature: name, email, and phone

The design should be minimal and clean.

Target Market(s)

Business owners who need our investment services.

Industry/Entity Type

Business

```html
<!DOCTYPE html>
<html lang="en">
<head>
<meta charset="utf-8">
<title>Brantwell Holdings – Business Card</title>
<link rel="stylesheet" href="https://fonts.googleapis.com/css2?family=Questrial&display=swap">
<style>
  :root {
    --backdrop: #e6e6e6;
    --card: #ffffff;
    --ink: #1a1a1a;
    --card-shadow: rgba(0, 0, 0, 0.18);
  }
  * { margin: 0; padding: 0; box-sizing: border-box; }
  html, body {
    width: 1200px;
    height: 1000px;
    overflow: hidden;
  }
  body {
    background: var(--backdrop);
    font-family: "Questrial", "Helvetica Neue", Arial, sans-serif;
    color: var(--ink);
    position: relative;
  }
  .card {
    position: absolute;
    left: 236px;
    width: 728px;
    height: 425px;
    background: var(--card);
    box-shadow: 0 6px 18px var(--card-shadow);
    overflow: hidden;
  }
  .card--back { top: 40px; }
  .card--front { top: 515px; }

  .wordmark {
    display: flex;
    align-items: center;
    gap: 18px;
    font-variant: small-caps;
    text-transform: lowercase;
    letter-spacing: 0.08em;
    white-space: nowrap;
    color: var(--ink);
  }
  .wordmark__square {
    flex: none;
    background: var(--ink);
  }
  .card--back .wordmark {
    position: absolute;
    left: 0;
    right: 0;
    top: 180px;
    justify-content: center;
    font-size: 52px;
  }
  .card--back .wordmark__square { width: 46px; height: 46px; }

  .card--front .wordmark {
    position: absolute;
    left: 40px;
    top: 44px;
    font-size: 26px;
    gap: 10px;
  }
  .card--front .wordmark__square { width: 24px; height: 24px; }

  .contact {
    position: absolute;
    left: 36px;
    top: 262px;
    font-variant: small-caps;
    letter-spacing: 0.06em;
    font-size: 25px;
    line-height: 43px;
    white-space: nowrap;
  }
  .contact__line { text-transform: lowercase; }
  .contact__label {
    display: inline-block;
    width: 112px;
  }
</style>
</head>
<body>
  <section class="card card--back" aria-label="Card back">
    <div class="wordmark">
      <span class="wordmark__square"></span>
      <span class="wordmark__name">Brantwell Holdings</span>
    </div>
  </section>

  <section class="card card--front" aria-label="Card front">
    <div class="wordmark">
      <span class="wordmark__square"></span>
      <span class="wordmark__name">Brantwell Holdings</span>
    </div>
    <div class="contact">
      <p class="contact__name">Alex Marlow</p>
      <p class="contact__line"><span class="contact__label">E-mail</span>: alex.marlow@brantwellholdings.com</p>
      <p class="contact__line"><span class="contact__label">Phone</span>: 07000 481 223</p>
    </div>
  </section>
</body>
</html>
```